Business card for plumber

I need a business card for my plumbing company.
on it should:
Surname
position
E-mail
Telephone & mobile phone
Website
Please everything as placeholders / fantasy names.
We stand for high quality, hygiene and professionalism.

Colours:
# 606060 anthracite
# f7931e orange
# 2b89cc blue

Industry/Entity Type

Plumber

Contact Information for Business Card

folgt...

```html
<!DOCTYPE html>
<html lang="en">
<head>
<meta charset="utf-8">
<title>Brennwald Haustechnik – Business Card</title>
<link rel="stylesheet" href="https://fonts.googleapis.com/css2?family=Roboto:wght@400;700&family=Roboto+Condensed:wght@700&display=swap">
<style>
  :root {
    --page-bg: #e6e2dc;
    --card-top: #f7f6f4;
    --card-bottom: #eceae7;
    --brand-blue: #2d67ad;
    --brand-orange: #e2581b;
    --orange-deep: #c9470f;
    --text-grey: #555a60;
    --rule-orange: #e06a2c;
    --web-text: #f3e6dc;
  }
  * { margin: 0; padding: 0; box-sizing: border-box; }
  html, body {
    width: 1200px; height: 970px; overflow: hidden;
    background: var(--page-bg);
  }
  .business-card {
    position: absolute;
    left: 100px; top: 200px;
    width: 1000px; height: 571px;
    border-radius: 22px;
    overflow: hidden;
    background: linear-gradient(160deg, var(--card-top), var(--card-bottom));
    box-shadow: 0 14px 40px rgba(0,0,0,0.18);
    font-family: "Roboto", Arial, sans-serif;
  }
  .company-name {
    position: absolute;
    right: 56px; top: 160px;
    text-align: right;
    color: var(--brand-blue);
    font-family: "Roboto Condensed", Arial, sans-serif;
    font-weight: 700;
    line-height: 1;
  }
  .company-name .name-line { display: block; font-size: 50px; }
  .company-name .sub-line { display: block; font-size: 25px; letter-spacing: 9.5px; margin-top: 6px; margin-right: -9px; }
  .person {
    position: absolute; left: 60px; top: 300px;
  }
  .person-name {
    font-family: "Roboto Condensed", Arial, sans-serif;
    font-weight: 700; font-size: 33px;
    color: var(--brand-blue); letter-spacing: 0.5px; line-height: 1;
  }
  .person-role {
    font-size: 22px; color: var(--brand-orange); margin-top: 4px;
  }
  .divider {
    position: absolute; left: 60px; top: 386px;
    width: 880px; height: 2px; background: var(--rule-orange);
  }
  .contact-list {
    position: absolute; left: 60px; top: 424px;
    list-style: none;
  }
  .contact-item {
    display: flex; align-items: center; gap: 14px;
    height: 32px;
    font-size: 25px; color: var(--text-grey);
  }
  .contact-icon { width: 24px; height: 24px; flex: none; }
  .footer-shapes { position: absolute; left: 0; bottom: 0; }
  .website {
    position: absolute; right: 78px; bottom: 14px;
    font-size: 22px; color: var(--web-text); letter-spacing: 0.5px;
  }
</style>
</head>
<body>
  <div class="business-card">
    <div class="company-name">
      <span class="name-line">BRENNWALD</span>
      <span class="sub-line">HAUSTECHNIK</span>
    </div>

    <div class="person">
      <div class="person-name">JONAS WEBER</div>
      <div class="person-role">Manager</div>
    </div>

    <div class="divider"></div>

    <ul class="contact-list">
      <li class="contact-item">
        <svg class="contact-icon" viewBox="0 0 24 24" aria-hidden="true">
          <circle cx="12" cy="12" r="12" fill="var(--brand-orange)"/>
          <rect x="8.5" y="6" width="7" height="12" rx="1.2" fill="none" stroke="#fff" stroke-width="1.6"/>
        </svg>
        +1 123 456 7890
      </li>
      <li class="contact-item">
        <svg class="contact-icon" viewBox="0 0 24 24" aria-hidden="true">
          <circle cx="12" cy="12" r="12" fill="var(--brand-orange)"/>
          <path d="M6 10 Q12 5 18 10 L16.5 12 L14.5 10.5 L9.5 10.5 L7.5 12 Z" fill="#fff"/>
          <rect x="8" y="12" width="8" height="5" rx="1" fill="#fff"/>
        </svg>
        +1 123 456 7890
      </li>
      <li class="contact-item">
        <svg class="contact-icon" viewBox="0 0 24 24" aria-hidden="true">
          <circle cx="12" cy="12" r="12" fill="var(--brand-orange)"/>
          <rect x="6.5" y="8" width="11" height="8" fill="none" stroke="#fff" stroke-width="1.4"/>
          <path d="M6.5 8 L12 12.5 L17.5 8 M6.5 16 L10.5 12 M17.5 16 L13.5 12" fill="none" stroke="#fff" stroke-width="1.2"/>
        </svg>
        info@brennwald-haus.com
      </li>
    </ul>

    <svg class="footer-shapes" width="1000" height="60" viewBox="0 0 1000 60" aria-hidden="true">
      <defs>
        <linearGradient id="footerOrange" x1="0" y1="0" x2="1" y2="0">
          <stop offset="0" stop-color="var(--brand-orange)"/>
          <stop offset="1" stop-color="var(--orange-deep)"/>
        </linearGradient>
      </defs>
      <path d="M0 42 L510 42 L494 60 L0 60 Z" fill="var(--brand-blue)"/>
      <path d="M517 60 Q540 8 585 6 L1000 6 L1000 60 Z" fill="url(#footerOrange)"/>
    </svg>
    <div class="website">www.brennwald-haus.com</div>
  </div>
</body>
</html>
```